We need a design for our security installation based business. Our name is K M Security Systems

We need a business card for a security installation based company. We want to look modern and professional. We would like our company logo used and the three main colours to be white, black and orange. We install intruder alarms, cctv and access control. Our preference would be to use the black/orange design on the front and orange/black on the back. Feel free to post variations.

Target Market(s)

Business owners, commercial property and large residential properties

Industry/Entity Type

Business

Contact Information for Business Card

Owen Pellworth 07812 904 226

Liam Foxcombe 07755 618 042

operations@kmsecuritysystems.example.co.uk

Intruder Alarms
CCTV
Access Control

Colors
f78f20
000000
ffffff

Requirements
Must have
• Must have the logo on the business card somewhere

```html
<!DOCTYPE html>
<html lang="en">
<head>
<meta charset="utf-8">
<title>K M Security Systems – Business Card</title>
<link rel="stylesheet" href="https://fonts.googleapis.com/css2?family=Barlow+Condensed:wght@700&family=Work+Sans:wght@400;500&display=swap">
<style>
  :root {
    --stage: #161616;
    --card: #242424;
    --card-edge: #2c2c2c;
    --orange: #f0512a;
    --white: #ffffff;
    --logo-grey: #8a8a8a;
    --text-soft: #e8e8e8;
  }
  * { margin: 0; padding: 0; box-sizing: border-box; }
  html, body {
    width: 1200px; height: 900px; overflow: hidden;
    background: var(--stage);
  }
  .stage {
    width: 1200px; height: 900px;
    display: flex; flex-direction: column; align-items: center; justify-content: center;
    gap: 40px;
  }
  .card {
    width: 680px; height: 388px;
    background: linear-gradient(135deg, var(--card) 0%, var(--card-edge) 100%);
    box-shadow: 0 10px 30px rgba(0,0,0,0.55);
    position: relative;
    font-family: "Work Sans", sans-serif;
    color: var(--white);
  }

  /* Front */
  .card-front {
    display: flex; flex-direction: column; align-items: center; justify-content: center;
  }
  .brand {
    display: flex; align-items: center; gap: 16px;
  }
  .brand-mark {
    width: 30px; height: 30px; background: var(--logo-grey);
  }
  .brand-name {
    font-family: "Work Sans", sans-serif; font-weight: 500;
    font-size: 40px; letter-spacing: 3px; color: var(--logo-grey);
    text-transform: uppercase;
  }
  .services {
    margin-top: 34px;
    font-size: 14px; letter-spacing: 2.5px; color: var(--text-soft);
  }
  .services .sep { color: var(--orange); margin: 0 8px; }

  /* Back */
  .card-back { padding: 0 60px; }
  .contacts {
    position: absolute; top: 112px; left: 0; right: 0;
    display: flex; justify-content: center; align-items: center; gap: 34px;
  }
  .contact { display: flex; flex-direction: column; }
  .contact-left { align-items: flex-end; }
  .contact-right { align-items: flex-start; margin-top: 28px; }
  .contact-name {
    font-family: "Barlow Condensed", sans-serif; font-weight: 700;
    font-size: 40px; letter-spacing: 1px; color: var(--orange);
    text-transform: uppercase; line-height: 1;
  }
  .contact-phone {
    margin-top: 10px;
    display: flex; align-items: center; gap: 14px;
    font-size: 16px; letter-spacing: 1.5px; color: var(--text-soft);
  }
  .phone-icon { width: 10px; height: 16px; }
  .divider {
    width: 2px; height: 70px; background: var(--white);
  }
  .email {
    position: absolute; left: 82px; bottom: 74px;
    font-size: 17px; letter-spacing: 1.2px; color: var(--text-soft);
  }
  .email-label { color: var(--orange); margin-right: 8px; }
</style>
</head>
<body>
<main class="stage">

  <section class="card card-front" aria-label="Card front">
    <div class="brand">
      <span class="brand-mark" aria-hidden="true"></span>
      <span class="brand-name">K M Security Systems</span>
    </div>
    <p class="services">
      Intruder Alarms<span class="sep">|</span>CCTV<span class="sep">|</span>Access Control
    </p>
  </section>

  <section class="card card-back" aria-label="Card back">
    <div class="contacts">
      <div class="contact contact-left">
        <span class="contact-name">Owen Pellworth</span>
        <span class="contact-phone">
          07812 904 226
          <svg class="phone-icon" viewBox="0 0 10 16" aria-hidden="true">
            <rect x="1" y="1" width="8" height="14" rx="1.2" fill="none" stroke="#f0512a" stroke-width="1.6"/>
            <line x1="3.5" y1="12.5" x2="6.5" y2="12.5" stroke="#f0512a" stroke-width="1.2"/>
          </svg>
        </span>
      </div>
      <span class="divider" aria-hidden="true"></span>
      <div class="contact contact-right">
        <span class="contact-name">Liam Foxcombe</span>
        <span class="contact-phone">
          <svg class="phone-icon" viewBox="0 0 10 16" aria-hidden="true">
            <rect x="1" y="1" width="8" height="14" rx="1.2" fill="none" stroke="#f0512a" stroke-width="1.6"/>
            <line x1="3.5" y1="12.5" x2="6.5" y2="12.5" stroke="#f0512a" stroke-width="1.2"/>
          </svg>
          07755 618 042
        </span>
      </div>
    </div>
    <p class="email"><span class="email-label">Email:</span>operations@kmsecuritysystems.example.co.uk</p>
  </section>

</main>
</body>
</html>
```